Pet business needs a business card

Pet shop needs a business card. Like dark background and and debased look.

Meadowpaws
Lindenweg 47
B - 3280 Velmor
Belgium

www.meadowpaws-example.com
mail@meadowpaws-example.com
Phone +32478610927

I will ad a tagline shortly.

Industry/Entity Type

Shop

Font styles to use
Sans Serif

Requirements
Must have
• Must be possible to print the card debased. See example image.

```html
<!DOCTYPE html>
<html lang="en">
<head>
<meta charset="utf-8">
<title>Meadowpaws – Business Card</title>
<link rel="stylesheet" href="https://fonts.googleapis.com/css2?family=Open+Sans:wght@400;600;800&display=swap">
<style>
  :root {
    --backdrop: #e3e3e3;
    --card-black: #1d1817;
    --accent-orange: #f5a54a;
    --stripe-grey: #8d8a80;
    --text-orange: #f5a54a;
  }
  * { margin: 0; padding: 0; box-sizing: border-box; }
  html, body {
    width: 1200px;
    height: 800px;
    overflow: hidden;
    background: var(--backdrop);
    font-family: "Open Sans", Arial, sans-serif;
  }
  .canvas {
    position: relative;
    width: 1200px;
    height: 800px;
  }
  .card {
    position: absolute;
    width: 540px;
    height: 310px;
    background: var(--card-black);
    overflow: hidden;
    box-shadow: 0 6px 18px rgba(0,0,0,0.25);
  }
  .card--front { left: 50px; top: 110px; }
  .card--back  { left: 610px; top: 380px; }

  .stripe { position: absolute; left: 0; right: 0; }
  .stripe--orange { height: 9px; background: var(--accent-orange); }
  .stripe--grey   { height: 4px; background: var(--stripe-grey); }
  .stripe--top-orange    { top: 30px; }
  .stripe--top-grey      { top: 44px; }
  .stripe--bottom-grey   { bottom: 44px; }
  .stripe--bottom-orange { bottom: 30px; }

  .brand {
    position: absolute;
    display: flex;
    align-items: center;
    gap: 12px;
    color: var(--text-orange);
    font-weight: 800;
    letter-spacing: 0.5px;
  }
  .brand__dot {
    display: block;
    border-radius: 50%;
    background: var(--stripe-grey);
  }
  .card--front .brand {
    left: 0; right: 0; top: 0; bottom: 0;
    justify-content: center;
    font-size: 54px;
  }
  .card--front .brand__dot { width: 22px; height: 22px; }

  .card--back .brand {
    left: 40px;
    top: 130px;
    font-size: 30px;
  }
  .card--back .brand__dot { width: 14px; height: 14px; }

  .contact {
    position: absolute;
    left: 300px;
    top: 72px;
    list-style: none;
    color: var(--text-orange);
    font-size: 14px;
    line-height: 1.3;
  }
  .contact__item {
    display: flex;
    align-items: flex-start;
    gap: 10px;
    margin-bottom: 7px;
  }
  .contact__icon {
    flex: 0 0 14px;
    width: 14px;
    height: 14px;
    margin-top: 2px;
    fill: var(--text-orange);
  }
  .contact__item--phone { font-size: 16px; }
</style>
</head>
<body>
<main class="canvas">

  <section class="card card--front" aria-label="Business card front">
    <div class="stripe stripe--orange stripe--top-orange"></div>
    <div class="stripe stripe--grey stripe--top-grey"></div>
    <div class="brand">
      <span class="brand__dot"></span>
      <span class="brand__name">Meadowpaws</span>
    </div>
    <div class="stripe stripe--grey stripe--bottom-grey"></div>
    <div class="stripe stripe--orange stripe--bottom-orange"></div>
  </section>

  <section class="card card--back" aria-label="Business card back">
    <div class="stripe stripe--orange stripe--top-orange"></div>
    <div class="stripe stripe--grey stripe--top-grey"></div>

    <div class="brand">
      <span class="brand__dot"></span>
      <span class="brand__name">Meadowpaws</span>
    </div>

    <ul class="contact">
      <li class="contact__item contact__item--address">
        <svg class="contact__icon" viewBox="0 0 24 24" aria-hidden="true"><path d="M12 2a7 7 0 0 0-7 7c0 5 7 13 7 13s7-8 7-13a7 7 0 0 0-7-7zm0 9.5A2.5 2.5 0 1 1 12 6.5a2.5 2.5 0 0 1 0 5z"/></svg>
        <span>Lindenweg 47<br>B - 3280 Velmor,<br>Belgium</span>
      </li>
      <li class="contact__item contact__item--phone">
        <svg class="contact__icon" viewBox="0 0 24 24" aria-hidden="true"><path d="M12 1a11 11 0 1 0 0 22 11 11 0 0 0 0-22zm4.6 15.3-1 1c-.4.4-1 .5-1.5.3-3-1.2-5.4-3.6-6.6-6.6-.2-.5-.1-1.1.3-1.5l1-1c.3-.3.8-.3 1.1 0l1.3 1.5c.3.3.3.7 0 1l-.7.8c.7 1.3 1.8 2.4 3.1 3.1l.8-.7c.3-.3.7-.3 1 0l1.5 1.3c.3.3.3.8 0 1.1z"/></svg>
        <span>+32478610927</span>
      </li>
      <li class="contact__item contact__item--email">
        <svg class="contact__icon" viewBox="0 0 24 24" aria-hidden="true"><path d="M2 5h20v14H2V5zm2 2v.4l8 5.2 8-5.2V7H4zm0 2.8V17h16V9.8l-8 5.2-8-5.2z"/></svg>
        <span>mail@meadowpaws-example.com</span>
      </li>
      <li class="contact__item contact__item--web">
        <svg class="contact__icon" viewBox="0 0 24 24" aria-hidden="true"><path d="M12 1a11 11 0 1 0 0 22 11 11 0 0 0 0-22zm0 2c1.2 0 2.6 2.3 3.1 6H8.9C9.4 5.3 10.8 3 12 3zM3.1 11h3.8a20 20 0 0 0 0 2H3.1a9 9 0 0 1 0-2zm5.8 0h6.2a18 18 0 0 1 0 2H8.9a18 18 0 0 1 0-2zm8.2 0h3.8a9 9 0 0 1 0 2h-3.8a20 20 0 0 0 0-2zM12 21c-1.2 0-2.6-2.3-3.1-6h6.2c-.5 3.7-1.9 6-3.1 6z"/></svg>
        <span>www.meadowpaws-example.com</span>
      </li>
    </ul>

    <div class="stripe stripe--grey stripe--bottom-grey"></div>
    <div class="stripe stripe--orange stripe--bottom-orange"></div>
  </section>

</main>
</body>
</html>
```